Event flyer for Sunday night Youth Group

Need a 4 x 6 or 5 x 7 flyer for a new youth group starting on April 14. The youth group is for students in middle school and high school so it needs to look fun and cool, but not childish. I prefer it not to include pictures of people unless it's so obscure you can't really see their faces. I've uploaded some pictures of flyers I like. I've also attached a couple versions of our logo to use on the flyer.
Information the flyer needs to include:
Youth Group
Sundays, 6-8pm (beginning April 14)
Location: Merriwick's - 4219 Hollowfern Ln S, Keizer, 97418
There will be dinner, games, friends, and a message.
Target Market(s)
Youth ages 13-18
Industry/Entity Type
Church
Colors
Designer to choose colors to be used in the design.
Look and feel

```html
<!DOCTYPE html>
<html lang="en">
<head>
<meta charset="utf-8">
<title>Youth Group – Wayfield Fellowship</title>
<link rel="stylesheet" href="https://fonts.googleapis.com/css2?family=Anton&family=Montserrat:wght@500;600&family=Yellowtail&display=swap">
<style>
  :root{
    --stage:#4a4b46;
    --yellow:#ffd000;
    --yellow-bright:#fff200;
    --navy:#13296b;
    --navy-deep:#1b3a8c;
  }
  *{margin:0;padding:0;box-sizing:border-box}
  html,body{width:1200px;height:1200px;overflow:hidden;background:var(--stage)}
  .flyer{
    position:absolute;left:249px;top:109px;width:702px;height:982px;overflow:hidden;
    background:linear-gradient(180deg,#d9d9d6 0%,#eeeeec 35%,#f4f4f2 60%,#e3e3df 100%);
    font-family:"Montserrat",sans-serif;color:var(--navy);
  }
  .photo{position:absolute;top:0;height:420px}
  .photo--bible{left:0;width:234px;background:linear-gradient(180deg,#6e6c66 0%,#a9a79f 45%,rgba(238,238,236,0) 100%)}
  .photo--figure{left:234px;width:234px;background:linear-gradient(180deg,#d6d6d4 0%,#c4c4c1 40%,rgba(238,238,236,0) 100%)}
  .photo--cross{left:468px;width:234px;background:linear-gradient(200deg,#e9c94a 0%,#9c9a8e 35%,rgba(238,238,236,0) 100%)}
  .paper{position:absolute;inset:0}
  .brand{
    position:absolute;left:0;top:43px;width:306px;height:76px;background:var(--yellow);
    clip-path:polygon(0 0,100% 0,86% 100%,0 100%);
    display:flex;align-items:center;gap:12px;padding-left:44px;z-index:2;
  }
  .brand__mark{width:30px;height:30px;background:var(--navy)}
  .brand__name{font-weight:600;font-size:17px;line-height:1.15;color:var(--navy);text-transform:uppercase;letter-spacing:.5px}
  .headline{position:absolute;inset:0;z-index:3}
  .headline__youth{
    position:absolute;left:0;top:230px;width:100%;text-align:center;
    font-family:"Anton",sans-serif;font-weight:400;font-size:183px;line-height:1;color:var(--yellow);
    letter-spacing:2px;transform:scaleX(1.17);transform-origin:347px 0;
    text-shadow:0 3px 6px rgba(120,100,0,.25);
  }
  .headline__group{
    position:absolute;left:350px;top:322px;font-family:"Yellowtail","Brush Script MT",cursive;font-weight:400;
    font-size:134px;line-height:1;color:var(--navy-deep);transform:rotate(-6deg);white-space:nowrap;
  }
  .tag{display:inline-block;background:var(--yellow);border-radius:6px;color:var(--navy);font-weight:600}
  .when{position:absolute;left:96px;top:521px;z-index:2}
  .when__day{font-size:29px;padding:0 10px;line-height:34px}
  .when__time{font-size:70px;font-weight:500;line-height:1;margin:6px 0 4px}
  .when__start{font-size:19px;font-weight:500;padding:1px 8px;margin-left:14px}
  .divider{position:absolute;left:358px;top:519px;width:3px;height:152px;background:var(--yellow)}
  .where{position:absolute;left:392px;top:521px;z-index:2}
  .where__label{font-size:29px;padding:0 8px;line-height:34px;display:inline-flex;align-items:center;gap:4px}
  .where__address{font-size:21px;font-weight:500;line-height:26px;margin:10px 0 0 7px}
  .details{position:absolute;left:0;top:700px;width:100%;text-align:center;z-index:2}
  .details__ages{font-size:21px;font-weight:500;padding:2px 18px}
  .details__text{font-size:23px;font-weight:500;line-height:31px;margin-top:9px}
  .icons{position:absolute;left:150px;top:815px;width:402px;height:60px;display:flex;align-items:center;justify-content:space-between;z-index:2}
  .icons svg{width:64px;height:58px;fill:none;stroke:var(--navy);stroke-width:2.4;stroke-linecap:round;stroke-linejoin:round}
  .icons .sep{width:2px;height:50px;background:var(--yellow)}
</style>
</head>
<body>
<main class="flyer">
  <div class="photo photo--bible" role="img" aria-label="Photo of hands holding an open Bible"></div>
  <div class="photo photo--figure" role="img" aria-label="Soft illustration of a robed figure with open arms among clouds"></div>
  <div class="photo photo--cross" role="img" aria-label="Photo of a stone cross against the sky"></div>

  <svg class="paper" viewBox="0 0 702 982" aria-hidden="true">
    <defs>
      <linearGradient id="leftPaper" x1="0" y1="0" x2="0.3" y2="1">
        <stop offset="0" stop-color="#d9c98a"/>
        <stop offset=".45" stop-color="#cfc6a4"/>
        <stop offset=".8" stop-color="#8a93a6"/>
        <stop offset="1" stop-color="#1b3566"/>
      </linearGradient>
      <linearGradient id="rightPaper" x1="0" y1="0" x2="1" y2="1">
        <stop offset="0" stop-color="#ffd000"/>
        <stop offset="1" stop-color="#fff200"/>
      </linearGradient>
    </defs>
    <path d="M0 420 L14 424 L10 438 L28 446 L22 470 L40 482 L36 520 L55 540 L62 600 L88 640 L110 690 L130 730 L150 780 L168 820 L186 870 L205 930 L220 982 L0 982 Z" fill="url(#leftPaper)" opacity=".9"/>
    <path d="M702 790 L690 800 L660 812 L640 835 L610 848 L580 870 L540 880 L500 900 L460 912 L420 920 L380 932 L330 940 L300 952 L250 968 L232 982 L702 982 Z" fill="url(#rightPaper)"/>
    <path d="M702 790 L690 800 L660 812 L640 835 L610 848 L580 870 L540 880 L500 900 L460 912 L420 920 L380 932 L330 940 L300 952 L250 968 L232 982" fill="none" stroke="#fffbe6" stroke-width="4"/>
  </svg>

  <div class="brand">
    <span class="brand__mark"></span>
    <span class="brand__name">Wayfield<br>Fellowship</span>
  </div>

  <div class="headline">
    <h1 class="headline__youth">YOUTH</h1>
    <div class="headline__group">Group</div>
  </div>

  <section class="when">
    <span class="tag when__day">Sundays</span>
    <p class="when__time">6-8pm</p>
    <span class="tag when__start">(beginning April 14)</span>
  </section>
  <div class="divider"></div>
  <section class="where">
    <span class="tag where__label">Location
      <svg width="24" height="24" viewBox="0 0 24 24" fill="none" stroke="#13296b" stroke-width="2"><path d="M12 21s-6-6-6-11a6 6 0 0 1 12 0c0 5-6 11-6 11z"/><circle cx="12" cy="10" r="2.2"/><path d="M7 21h10"/></svg>
    </span>
    <p class="where__address">Merriwick's - 4219<br>Hollowfern Ln S,<br>Keizer, 97418</p>
  </section>

  <section class="details">
    <span class="tag details__ages">Youth ages 13-18</span>
    <p class="details__text">There will be dinner, games,<br>friends, and a message.</p>
  </section>

  <div class="icons">
    <svg viewBox="0 0 64 58" aria-label="Dinner"><path d="M4 50h56M10 50V28h10v22M15 28v-6M15 20c-2-3 2-5 0-8"/><path d="M26 44a15 15 0 0 1 30 0zM41 29v-4M38 25h6"/></svg>
    <span class="sep"></span>
    <svg viewBox="0 0 64 58" aria-label="Friends"><circle cx="20" cy="24" r="5"/><circle cx="44" cy="24" r="5"/><path d="M8 52V40c0-6 5-9 10-9l8-10 6-6M56 52V40c0-6-5-9-10-9l-8-10-6-6M26 52V42M38 52V42M32 4v5M24 7l3 4M40 7l-3 4"/></svg>
    <span class="sep"></span>
    <svg viewBox="0 0 64 58" aria-label="Games"><path d="M18 16h28c8 0 12 8 14 20 1 8-6 12-11 6l-5-6H20l-5 6c-5 6-12 2-11-6 2-12 6-20 14-20z"/><path d="M20 24v10M15 29h10"/><circle cx="42" cy="26" r="1.8"/><circle cx="48" cy="30" r="1.8"/><circle cx="42" cy="33" r="1.8"/></svg>
    <span class="sep"></span>
    <svg viewBox="0 0 64 58" aria-label="Message"><path d="M32 6a22 22 0 1 1-12 40l-10 4 3-10A22 22 0 0 1 32 6z"/><circle cx="23" cy="28" r="1.8"/><circle cx="32" cy="28" r="1.8"/><circle cx="41" cy="28" r="1.8"/></svg>
  </div>
</main>
</body>
</html>
```